Bright Path Trading
Business Cards and Stationary
Project: Bright Path Trading
Bright Path Trading -
Creative Brief
Modern
Rob and Kara Halvorsen, Owners
47 Elmcrest Road Northampton, MA 01384
rob@brightpathtrading.com
www.brightpathtrading.com
Please put Kara's email underneath Rob's email: kara@brightpathtrading.com

```html
<!DOCTYPE html>
<html lang="en">
<head>
<meta charset="utf-8">
<title>Bright Path Trading – Business Card</title>
<link rel="stylesheet" href="https://fonts.googleapis.com/css2?family=Arimo:wght@400;700&display=swap">
<style>
  :root {
    --maroon-deep: #5e1416;
    --maroon-light: #a4484a;
    --card-white: #ffffff;
    --card-grey: #e4e4e4;
    --ink: #111111;
    --accent: #7a2224;
  }
  * { margin: 0; padding: 0; box-sizing: border-box; }
  html, body { width: 1200px; height: 686px; overflow: hidden; }
  body { background: var(--card-white); }
  .card {
    position: relative;
    width: 1200px;
    height: 686px;
    overflow: hidden;
    background: radial-gradient(ellipse at 50% 40%, var(--card-white) 35%, var(--card-grey) 100%);
    font-family: "Arimo", Arial, sans-serif;
    color: var(--ink);
  }
  .card__header { position: absolute; inset: 0 0 auto 0; width: 1200px; height: 170px; }
  .brand {
    position: absolute;
    top: 300px;
    left: 0;
    width: 1200px;
    display: flex;
    justify-content: center;
    align-items: center;
    gap: 20px;
  }
  .brand__dot {
    width: 34px; height: 34px; border-radius: 50%;
    background: var(--accent);
  }
  .brand__name {
    font-family: "Arimo", Arial, sans-serif;
    font-weight: 700;
    font-size: 60px;
    color: var(--ink);
  }
  .contact {
    position: absolute;
    left: 43px;
    top: 480px;
    font-size: 23px;
    line-height: 27px;
    font-style: normal;
  }
  .owners {
    position: absolute;
    right: 43px;
    top: 592px;
    text-align: right;
    font-size: 23px;
    line-height: 30px;
  }
  .owners__names { font-weight: 700; font-size: 24px; }
</style>
</head>
<body>
<main class="card">
  <svg class="card__header" viewBox="0 0 1200 170" aria-hidden="true">
    <defs>
      <radialGradient id="bandGlow" cx="50%" cy="20%" r="60%">
        <stop offset="0" stop-color="var(--maroon-light)"/>
        <stop offset="1" stop-color="var(--maroon-deep)"/>
      </radialGradient>
      <linearGradient id="swooshGrey" x1="0" y1="0" x2="0" y2="1">
        <stop offset="0" stop-color="#d8d8d8"/>
        <stop offset="1" stop-color="#ffffff" stop-opacity="0"/>
      </linearGradient>
    </defs>
    <path d="M0 0 H1200 V100 Q600 20 0 108 Z" fill="url(#bandGlow)"/>
    <path d="M0 120 Q600 35 1200 112 V150 Q600 70 0 160 Z" fill="url(#swooshGrey)"/>
    <path d="M0 108 Q600 20 1200 100" fill="none" stroke="var(--card-white)" stroke-width="8"/>
  </svg>

  <div class="brand">
    <span class="brand__dot"></span>
    <span class="brand__name">Bright Path Trading</span>
  </div>

  <address class="contact">
    <p>47 Elmcrest Road Northampton,</p>
    <p>MA 01384</p>
    <p>P : 413.555.0142</p>
    <p>F : 413.555.0143</p>
    <p>E : rob@brightpathtrading.com</p>
    <p>&nbsp;&nbsp;&nbsp;&nbsp;&nbsp;kara@brightpathtrading.com</p>
    <p>W: www.brightpathtrading.com</p>
  </address>

  <div class="owners">
    <p class="owners__names">Rob and Kara Halvorsen</p>
    <p class="owners__title">Owners</p>
  </div>
</main>
</body>
</html>
```